Visitenkarten-Design für das Business mit Gesundheit& Beauty
Zielgruppe
Ich bin selbständige Vertriebspartnerin von Vb. Die Visitenkarten sollen nicht zu verspielt wirken, eher geschäftlich. Dennoch könnte eine Verbindung zu den Bereichen Gesundheit & Beuuty dazukommen .
Hauptproduktmerkmal ist zum Beispiel die Aloe Vera, Naturprodukte.. mehr Infos auf : www.katrin-obelmoor.de
Instagram :kati_obelmoor
Eventuell könnte mein Slogan mit 'just more' noch einfließen, muss aber nicht. Bin für Ideen offen...
Aufgabenstellung
elegant und zeitlos, aber weich
Vielleicht eine goldene Aloe Vera irgendwie mit drauf?
Habe bei den dateien mal ein paar Screenshots hinzugefügt was ich recht schön fand

```html
<!DOCTYPE html>
<html lang="de">
<head>
<meta charset="utf-8">
<title>Katrin Obelmoor – Visitenkarte</title>
<link rel="stylesheet" href="https://fonts.googleapis.com/css2?family=Montserrat:wght@400;500;700&display=swap">
<style>
  :root {
    --canvas: #e9e6e1;
    --card-white: #ffffff;
    --ink: #1f1f22;
    --ink-soft: #4a4a4e;
    --gold: #a9957a;
    --beige-light: #eee4d2;
    --beige-mid: #dccbb0;
    --leaf-sage: rgba(185,185,142,.45);
    --leaf-gold: rgba(201,180,143,.5);
  }
  * { box-sizing: border-box; margin: 0; padding: 0; }
  html, body { width: 1200px; height: 900px; overflow: hidden; }
  body {
    background: var(--canvas);
    display: flex;
    flex-direction: column;
    align-items: center;
    justify-content: center;
    gap: 44px;
    font-family: "Montserrat", sans-serif;
    color: var(--ink);
  }
  .card {
    position: relative;
    width: 700px;
    height: 400px;
    box-shadow: 0 10px 28px rgba(0,0,0,.14);
    overflow: hidden;
  }
  .card--front { background: var(--card-white); }
  .card--back { background: var(--beige-light); }

  .logo-frame {
    position: absolute;
    width: 390px;
    height: 92px;
    border: 2px solid var(--ink);
    display: flex;
    align-items: center;
    justify-content: center;
  }
  .logo-frame__name {
    font-family: "Montserrat", sans-serif;
    font-weight: 500;
    font-size: 28px;
    letter-spacing: 3px;
    text-transform: uppercase;
    color: var(--ink);
    white-space: nowrap;
  }
  .card--front .logo-frame { top: 58px; right: 58px; }
  .card--back .logo-frame { top: 150px; left: 90px; }

  .person {
    position: absolute;
    right: 392px;
    top: 236px;
    text-align: right;
  }
  .person__name { font-size: 26px; font-weight: 700; white-space: nowrap; }
  .person__first { color: var(--gold); }
  .person__last { color: var(--ink); }
  .person__role { font-size: 14px; color: var(--ink-soft); margin-top: 4px; letter-spacing: .4px; }

  .divider {
    position: absolute;
    left: 330px;
    top: 226px;
    width: 2px;
    height: 82px;
    background: var(--gold);
  }
  .contact {
    position: absolute;
    left: 352px;
    top: 222px;
    list-style: none;
    display: flex;
    flex-direction: column;
    gap: 8px;
  }
  .contact__item {
    display: flex;
    align-items: center;
    gap: 12px;
    font-size: 15px;
    color: var(--ink);
    letter-spacing: .3px;
    white-space: nowrap;
  }
  .contact__icon { width: 16px; height: 16px; fill: none; stroke: var(--gold); stroke-width: 1.8; }

  .artwork {
    position: absolute;
    inset: 0;
    background:
      radial-gradient(ellipse at 85% 25%, var(--leaf-sage), transparent 55%),
      radial-gradient(ellipse at 15% 90%, var(--leaf-gold), transparent 60%),
      linear-gradient(135deg, var(--beige-light), var(--beige-mid));
  }
</style>
</head>
<body>

  <section class="card card--front" aria-label="Vorderseite">
    <div class="logo-frame" role="img" aria-label="Logo Katrin Obelmoor">
      <span class="logo-frame__name">Katrin Obelmoor</span>
    </div>

    <div class="person">
      <p class="person__name"><span class="person__first">Jonas</span> <span class="person__last">Weidler</span></p>
      <p class="person__role">Owner-Director</p>
    </div>

    <div class="divider"></div>

    <ul class="contact">
      <li class="contact__item">
        <svg class="contact__icon" viewBox="0 0 16 16"><path d="M4 1.5 L6.5 4.5 L5 6.5 C6 8.5 7.5 10 9.5 11 L11.5 9.5 L14.5 12 L13 14.5 C7 14 2 9 1.5 3 Z"/></svg>
        0790 318 455
      </li>
      <li class="contact__item">
        <svg class="contact__icon" viewBox="0 0 16 16"><rect x="1.5" y="3.5" width="13" height="9" rx="1"/><path d="M1.5 4 L8 9 L14.5 4"/></svg>
        kontakt@obelmoor-mail.de
      </li>
      <li class="contact__item">
        <svg class="contact__icon" viewBox="0 0 16 16"><circle cx="8" cy="8" r="6.5"/><ellipse cx="8" cy="8" rx="2.8" ry="6.5"/><path d="M1.5 8 H14.5"/></svg>
        www.katrin-obelmoor.de
      </li>
    </ul>
  </section>

  <section class="card card--back" aria-label="Rückseite">
    <div class="artwork" role="img" aria-label="Zartes Blätter- und Aloe-Vera-Muster in Gold- und Salbeitönen auf beigem Grund"></div>
    <div class="logo-frame" role="img" aria-label="Logo Katrin Obelmoor">
      <span class="logo-frame__name">Katrin Obelmoor</span>
    </div>
  </section>

</body>
</html>
```